Design some Business Cards for Makeup Artist

I am a makeup artist and need a new business card designed, with a logo for my new business.

Size:
90mm x 55mm - landscape

Colour Palate:
Please use only Black, white and red colours (black and white being primary colours)

Brief:
I would like a minimalist design, with text on back and logo on front.
Logo to represent the makeup industry e.g. brush, powder puff etc. Simple, icon based logo design, please refer to image examples for similar styles of business cards.
Name (Corvella Shintre) can be in personalised font, see attached example.

Target audience:
Models, photographers, stylists, fashion

Text:
Corvella Shintre
Makeup Artist
0472 519 384
(plazzbook logo) CorvellaShintreMakeupArtist

Artwork to be supplied with 3mm bleed and crop marks

```html
<!DOCTYPE html>
<html lang="en">
<head>
<meta charset="utf-8">
<title>Corvella Shintre – Business Card</title>
<link rel="stylesheet" href="https://fonts.googleapis.com/css2?family=Gochi+Hand&family=Open+Sans:ital,wght@0,400;1,400&display=swap">
<style>
  :root {
    --page-bg: #ffffff;
    --card-bg: #231f20;
    --accent-pink: #e5478c;
    --text-white: #ffffff;
    --text-soft: #f2f2f2;
  }
  * { margin: 0; padding: 0; box-sizing: border-box; }
  html, body {
    width: 974px;
    height: 1200px;
    overflow: hidden;
    background: var(--page-bg);
  }
  .sheet {
    position: relative;
    width: 974px;
    height: 1200px;
  }
  .card {
    position: absolute;
    background: var(--card-bg);
    border-radius: 40px;
    overflow: hidden;
  }
  .card--front { left: 80px; top: 71px; width: 836px; height: 509px; }
  .card--back  { left: 75px; top: 613px; width: 837px; height: 511px; }

  /* Front logo */
  .logo-mark {
    position: absolute;
    left: 268px;
    top: 173px;
    width: 104px;
    height: 104px;
    border-radius: 50%;
    background: var(--accent-pink);
  }
  .logo-name {
    position: absolute;
    left: 365px;
    top: 277px;
    font-family: "Gochi Hand", cursive;
    font-size: 24px;
    color: var(--text-white);
    letter-spacing: 1.5px;
    line-height: 1;
  }

  /* Back content */
  .brand-title {
    position: absolute;
    left: 88px;
    top: 60px;
    font-family: "Gochi Hand", cursive;
    font-size: 64px;
    letter-spacing: 4px;
    color: var(--text-white);
    line-height: 1;
  }
  .audience {
    position: absolute;
    left: 88px;
    top: 127px;
    font-family: "Open Sans", sans-serif;
    font-size: 19px;
    color: var(--text-soft);
  }
  .divider {
    position: absolute;
    left: 88px;
    top: 216px;
    width: 81px;
    height: 2px;
    background: var(--text-white);
  }
  .person {
    position: absolute;
    left: 88px;
    top: 275px;
    font-family: "Open Sans", sans-serif;
    color: var(--text-soft);
  }
  .person__name { font-size: 19px; line-height: 26px; }
  .person__role { font-size: 16px; font-style: italic; line-height: 22px; }

  .contacts {
    position: absolute;
    left: 88px;
    top: 355px;
    list-style: none;
    font-family: "Open Sans", sans-serif;
    font-size: 19px;
    color: var(--text-soft);
  }
  .contacts__item {
    display: flex;
    align-items: center;
    height: 28px;
  }
  .contacts__icon {
    width: 18px;
    height: 18px;
    margin-right: 10px;
    flex: none;
  }
  .contacts__square {
    width: 17px;
    height: 17px;
    margin-right: 11px;
    background: var(--accent-pink);
    flex: none;
  }
</style>
</head>
<body>
<main class="sheet">
  <section class="card card--front" aria-label="Card front">
    <div class="logo-mark"></div>
    <p class="logo-name">Corvella Shintre</p>
  </section>

  <section class="card card--back" aria-label="Card back">
    <h1 class="brand-title">Corvella Shintre</h1>
    <p class="audience">Models · Photographers · Stylists · Fashion</p>
    <div class="divider"></div>
    <div class="person">
      <p class="person__name">Corvella Shintre</p>
      <p class="person__role">Makeup Artist</p>
    </div>
    <ul class="contacts">
      <li class="contacts__item">
        <svg class="contacts__icon" viewBox="0 0 24 24" aria-hidden="true">
          <path fill="var(--accent-pink)" d="M6.6 10.8a15.2 15.2 0 0 0 6.6 6.6l2.2-2.2a1 1 0 0 1 1-.25 11.4 11.4 0 0 0 3.6.57 1 1 0 0 1 1 1V20a1 1 0 0 1-1 1A17 17 0 0 1 3 4a1 1 0 0 1 1-1h3.5a1 1 0 0 1 1 1c0 1.25.2 2.45.57 3.57a1 1 0 0 1-.25 1z"/>
        </svg>
        <span>0472 519 384</span>
      </li>
      <li class="contacts__item">
        <svg class="contacts__icon" viewBox="0 0 24 18" aria-hidden="true">
          <rect x="1" y="1" width="22" height="16" fill="none" stroke="var(--accent-pink)" stroke-width="2"/>
          <path d="M1 1 L12 10 L23 1 M1 17 L9 8 M23 17 L15 8" fill="none" stroke="var(--accent-pink)" stroke-width="2"/>
        </svg>
        <span>corvellaxshintre@mailvo.com</span>
      </li>
      <li class="contacts__item">
        <span class="contacts__square" aria-hidden="true"></span>
        <span>CorvellaShintreMakeupArtist</span>
      </li>
    </ul>
  </section>
</main>
</body>
</html>
```